New Business Card Design For Re-Branded Company (New Logo)

We recently switched our DBA and had a new logo designed. We now need new business cards made around our new logo. We would like to stick with the color scheme in our logo: White, Orange, and Blue. We want to see original bold designs that reflect our position in the solar energy sector but we prefer simple over complicated.

We are curious about vertical designs so if you can translate your design onto a vertical layout we would be open to look at it. We especially like a few designs we have seen on here that are vertical with a black or very dark gray background. They have our logo on one side and then the normal vertical business card on the other side.

I have included a screenshot of one of the samples we like, labeled sample.jpg and a file we were given as an example of our logo on a dark background.

At the same time we are satisfied to stay with what we have always had in a horizontal format. If it's not a lot of extra work for you, designs that are submitted in both horizontal and vertical formats will be greatly appreciated.

Please submit your original, bold, clean designs for consideration. Contact us with any questions or comments that may arise.

Thank you and Good Luck,

KP

```html
<!DOCTYPE html>
<html lang="en">
<head>
<meta charset="utf-8">
<title>Kestrel Power business cards</title>
<link href="https://fonts.googleapis.com/css2?family=Open+Sans:wght@400;600;700&display=swap" rel="stylesheet">
<style>
  :root {
    --ink: #050505;
    --orange: #f07d22;
    --blue: #1b75bc;
    --white: #ffffff;
    --stage: #e6e4e0;
  }
  * { margin: 0; padding: 0; box-sizing: border-box; }
  html, body { width: 1200px; height: 892px; overflow: hidden; background: var(--stage); }
  body { font-family: "Open Sans", sans-serif; position: relative; }

  .card {
    position: absolute;
    top: 96px;
    width: 400px;
    height: 700px;
    background: var(--ink);
    overflow: hidden;
    box-shadow: 0 10px 30px rgba(0,0,0,.25);
  }
  .card--front { left: 150px; }
  .card--back { left: 650px; }

  .brand {
    display: flex;
    align-items: center;
    gap: 10px;
    font-family: "Open Sans", sans-serif;
    font-weight: 700;
    color: var(--orange);
    letter-spacing: .5px;
    text-transform: uppercase;
  }
  .brand__dot {
    width: 26px; height: 26px;
    border-radius: 50%;
    background: var(--blue);
    flex: none;
  }
  .card--front .brand { position: absolute; top: 110px; left: 40px; font-size: 34px; }

  .person { position: absolute; top: 200px; left: 40px; }
  .person__name { color: var(--orange); font-size: 38px; font-weight: 600; line-height: 1.1; }
  .person__title { color: var(--white); font-size: 20px; margin-top: 2px; }

  .phones { position: absolute; top: 320px; left: 40px; list-style: none; }
  .phones li {
    display: flex; align-items: center; gap: 16px;
    color: var(--white); font-size: 20px; height: 34px; letter-spacing: 1px;
  }
  .icon {
    width: 20px; height: 20px; flex: none;
    background: var(--orange);
    display: flex; align-items: center; justify-content: center;
  }
  .icon--light { background: var(--white); }

  .footer-band { position: absolute; left: 0; bottom: 0; width: 400px; height: 260px; }

  .contact {
    position: absolute; right: 36px; bottom: 60px;
    list-style: none; text-align: right;
    color: var(--white); font-size: 19px; line-height: 1.45;
  }
  .contact__row { display: flex; justify-content: flex-end; align-items: center; gap: 14px; }
  .contact__row--text { padding-right: 34px; }

  .card--back .brand {
    position: absolute; top: 300px; left: 0; width: 100%;
    justify-content: center; font-size: 36px;
  }
  .web {
    position: absolute; top: 540px; width: 100%; text-align: center;
    color: var(--white); font-size: 22px; letter-spacing: 1px;
  }
</style>
</head>
<body>

<section class="card card--front" aria-label="Business card front">
  <div class="brand"><span class="brand__dot"></span>Kestrel Power</div>

  <div class="person">
    <p class="person__name">Liam Porter</p>
    <p class="person__title">President</p>
  </div>

  <ul class="phones">
    <li><span class="icon"><svg width="12" height="12" viewBox="0 0 12 12"><path d="M2 1h2l1 3-1.5 1a7 7 0 0 0 3.5 3.5L8 7l3 1v2a1 1 0 0 1-1 1A9 9 0 0 1 1 2a1 1 0 0 1 1-1z" fill="#fff"/></svg></span>94 3120 7765</li>
    <li><span class="icon"><svg width="12" height="12" viewBox="0 0 12 12"><rect x="3" y="0.5" width="6" height="11" rx="1" fill="#fff"/><rect x="4" y="2" width="4" height="7" fill="#f07d22"/></svg></span>74 2681 4039</li>
    <li><span class="icon"><svg width="12" height="12" viewBox="0 0 12 12"><rect x="1" y="4" width="10" height="6" fill="#fff"/><rect x="3" y="1" width="6" height="4" fill="#fff"/><rect x="3" y="6" width="6" height="1" fill="#f07d22"/></svg></span>94 8852 1176</li>
  </ul>

  <svg class="footer-band" viewBox="0 0 400 260" aria-hidden="true">
    <path d="M0 40 Q180 -10 400 70 L400 260 L0 260 Z" fill="var(--blue)"/>
    <path d="M0 40 Q180 -10 400 70" fill="none" stroke="var(--orange)" stroke-width="4"/>
  </svg>

  <ul class="contact">
    <li class="contact__row contact__row--text">PO Box 3172</li>
    <li class="contact__row">Carlingford Vale NSW 2118
      <span class="icon icon--light"><svg width="12" height="12" viewBox="0 0 12 12"><path d="M6 0.5a4 4 0 0 1 4 4c0 3-4 7-4 7s-4-4-4-7a4 4 0 0 1 4-4z" fill="#1b75bc"/><circle cx="6" cy="4.5" r="1.5" fill="#fff"/></svg></span>
    </li>
    <li class="contact__row">kestrelpower@email.com
      <span class="icon icon--light"><svg width="12" height="12" viewBox="0 0 12 12"><rect x="1" y="2.5" width="10" height="7" fill="#1b75bc"/><path d="M1 2.5l5 4 5-4" fill="none" stroke="#fff" stroke-width="1"/></svg></span>
    </li>
  </ul>
</section>

<section class="card card--back" aria-label="Business card back">
  <div class="brand"><span class="brand__dot"></span>Kestrel Power</div>
  <p class="web">www.kestrelpower.com</p>
</section>

</body>
</html>
```